Dravetti Business Cards

We need a business card design for Dravetti Mining.

This is a B2B company that buys and sells large machinery tires within the coal mining industry. The design should the strong, crisp and masculine. I have uploaded the company logo and rough mock-up of what the back of the card should look like. the front of the card should have the same look/feel as the back. I need editable templates for both the front and the back of the card.

Color scheme should be grey/green/black

Contact information to include on the card:
Name: Owen Pellsworth
Title: Managing Director
Phone: 972-555-0143
Address: 3157 Brantley #5 Dallas, TX 75209
Email: Owen@Dravetti-example.com

I am also opening a contest for letterhead design. If you submit a business card design, please also submit a letterhead design with the same look/feel. The winner of the business card design will also will the letter head and be paid for both.

Target Market(s)

Procurement men/women in the coal mining industry

Industry/Entity Type

Coal Mining

```html
<!DOCTYPE html>
<html lang="en">
<head>
<meta charset="utf-8">
<title>Dravetti Mining Business Cards</title>
<link rel="stylesheet" href="https://fonts.googleapis.com/css2?family=Montserrat:wght@400;500;700&display=swap">
<style>
  :root {
    --backdrop: #d9d9d7;
    --card-light: #434644;
    --card-dark: #242625;
    --ink: #f2f2f0;
    --accent: #6cc04a;
    --muted: #c9cbc8;
  }
  * { box-sizing: border-box; margin: 0; padding: 0; }
  html, body {
    width: 1200px; height: 937px; overflow: hidden;
    background: var(--backdrop);
    font-family: "Montserrat", Arial, sans-serif;
  }
  .sheet {
    width: 1200px; height: 937px;
    display: flex; flex-direction: column; align-items: center; justify-content: center;
    gap: 56px;
  }
  .card {
    position: relative;
    width: 640px; height: 366px;
    border-radius: 4px;
    background: radial-gradient(ellipse at 55% 40%, var(--card-light) 0%, var(--card-dark) 85%);
    box-shadow: 0 10px 24px rgba(0,0,0,0.22);
    color: var(--ink);
  }
  .wordmark {
    display: flex; align-items: center; gap: 14px;
    font-weight: 700; letter-spacing: 0.06em; text-transform: uppercase;
    color: var(--ink);
  }
  .wordmark-square { background: var(--accent); flex: none; }

  /* front: contact side */
  .card-front .wordmark { position: absolute; left: 60px; top: 62px; font-size: 34px; }
  .card-front .wordmark-square { width: 26px; height: 26px; }
  .identity { position: absolute; left: 60px; top: 148px; display: flex; align-items: baseline; gap: 14px; }
  .person-name { font-size: 27px; font-weight: 500; }
  .person-title { font-size: 10px; font-weight: 500; letter-spacing: 0.06em; text-transform: uppercase; color: var(--muted); }
  .contact-list { position: absolute; left: 60px; top: 200px; list-style: none; }
  .contact-item { display: flex; align-items: center; gap: 14px; font-size: 19px; font-weight: 500; line-height: 34px; }
  .contact-icon { width: 20px; height: 20px; fill: var(--accent); flex: none; }
  .person-row { position: absolute; left: 60px; top: 152px; }

  /* back: logo side */
  .card-back .wordmark {
    position: absolute; left: 50%; top: 50%; transform: translate(-50%, -50%);
    font-size: 48px; white-space: nowrap;
  }
  .card-back .wordmark-square { width: 38px; height: 38px; }
</style>
</head>
<body>
<main class="sheet">
  <section class="card card-front" aria-label="Business card front">
    <div class="wordmark"><span class="wordmark-square"></span>Dravetti Mining</div>
    <div class="identity">
      <svg class="contact-icon" viewBox="0 0 20 20" aria-hidden="true"><circle cx="10" cy="6" r="4"/><path d="M2 19c0-5 3.5-7 8-7s8 2 8 7z"/></svg>
      <span class="person-name">Owen Pellsworth</span>
      <span class="person-title">Managing Director</span>
    </div>
    <ul class="contact-list">
      <li class="contact-item">
        <svg class="contact-icon" viewBox="0 0 20 20" aria-hidden="true"><path d="M5 2l3 4-2 2c1 2.5 3.5 5 6 6l2-2 4 3-2 3C9 17 3 11 2 4z"/></svg>
        972-555-0143
      </li>
      <li class="contact-item">
        <svg class="contact-icon" viewBox="0 0 20 20" aria-hidden="true"><path d="M10 1a6.5 6.5 0 0 0-6.5 6.5C3.5 12 10 19 10 19s6.5-7 6.5-11.5A6.5 6.5 0 0 0 10 1zm0 9a2.5 2.5 0 1 1 0-5 2.5 2.5 0 0 1 0 5z"/></svg>
        3157 Brantley #5 Dallas, TX 75209
      </li>
      <li class="contact-item">
        <svg class="contact-icon" viewBox="0 0 20 20" aria-hidden="true"><path d="M1 4h18v12H1z M2 5l8 6 8-6" stroke="#242625" stroke-width="1.4"/></svg>
        Owen@Dravetti-example.com
      </li>
    </ul>
  </section>

  <section class="card card-back" aria-label="Business card back">
    <div class="wordmark"><span class="wordmark-square"></span>Dravetti Mining</div>
  </section>
</main>
</body>
</html>
```